I need this done FAST!
Business Cards and Stationary for new home construction company - Construction
Simple
Gerald Finch
Owner
4816 Marlow Ct #306142 Houston, TX 77391
Gerald@thequillstoneframeworks.com
www.thequillstoneframeworks.com
I would like this business card to be minimal in its design. I just want it to be a way of saying ... Hi, call me directly. It does not need to be an advertisement. I need the vector files of this please
Front should be the logo only, and the back should be this information: Design~Build Firm Gerald Finch, Owner Phone Email Web address

```html
<!DOCTYPE html>
<html lang="en">
<head>
<meta charset="utf-8">
<title>Quillstone Frameworks – Business Card</title>
<link rel="stylesheet" href="https://fonts.googleapis.com/css2?family=Open+Sans:ital,wght@0,400;0,600;0,700;1,400&display=swap">
<style>
  :root {
    --backdrop: #e4e5e7;
    --card: #ffffff;
    --brand-red: #d0232a;
    --ink: #3a3a3a;
    --muted: #8c8c8c;
    --rule-grey: #c9c9c9;
  }
  * { box-sizing: border-box; margin: 0; padding: 0; }
  html, body {
    width: 1200px; height: 878px; overflow: hidden;
    background: var(--backdrop);
    font-family: "Open Sans", sans-serif;
  }
  .sheet {
    width: 1200px; height: 878px;
    display: flex; flex-direction: column; align-items: center; justify-content: center;
    gap: 50px;
  }
  .card {
    position: relative;
    width: 620px; height: 354px;
    background: var(--card);
    box-shadow: 0 4px 14px rgba(0,0,0,0.12);
    overflow: hidden;
  }
  .brand {
    display: flex; align-items: center; gap: 10px;
  }
  .brand-square {
    width: 22px; height: 22px; background: var(--brand-red);
  }
  .brand-name {
    font-weight: 700; color: var(--brand-red);
    letter-spacing: 0.04em; text-transform: uppercase;
  }
  /* Front */
  .card-front { display: flex; align-items: center; justify-content: center; }
  .card-front .brand-name { font-size: 30px; }
  .card-front .brand-square { width: 30px; height: 30px; }
  /* Back */
  .card-back .brand { position: absolute; left: 36px; top: 40px; }
  .card-back .brand-name { font-size: 19px; }
  .contact-list {
    position: absolute; left: 40px; top: 112px;
    list-style: none; font-size: 13px; color: var(--ink); line-height: 22px;
  }
  .contact-list li { display: flex; align-items: center; gap: 8px; }
  .contact-list svg { width: 12px; height: 12px; fill: var(--muted); }
  .person {
    position: absolute; right: 48px; top: 128px; text-align: left; width: 230px;
  }
  .person-name { font-size: 20px; font-weight: 600; color: var(--muted); }
  .person-role { font-size: 13px; font-style: italic; color: var(--brand-red); margin-top: 2px; }
  .address {
    position: absolute; right: 48px; top: 228px; width: 230px;
    font-size: 13px; color: var(--ink); line-height: 19px;
  }
  .swoosh { position: absolute; left: 0; bottom: 0; width: 620px; height: 120px; }
</style>
</head>
<body>
<main class="sheet">
  <section class="card card-front" aria-label="Card front">
    <div class="brand">
      <span class="brand-square"></span>
      <span class="brand-name">Quillstone Frameworks</span>
    </div>
  </section>

  <section class="card card-back" aria-label="Card back">
    <div class="brand">
      <span class="brand-square"></span>
      <span class="brand-name">Quillstone Frameworks</span>
    </div>

    <ul class="contact-list">
      <li><svg viewBox="0 0 24 24"><path d="M6.6 10.8a15 15 0 0 0 6.6 6.6l2.2-2.2a1 1 0 0 1 1-.25 11.4 11.4 0 0 0 3.6.57 1 1 0 0 1 1 1V20a1 1 0 0 1-1 1A17 17 0 0 1 3 4a1 1 0 0 1 1-1h3.5a1 1 0 0 1 1 1c0 1.25.2 2.45.57 3.57a1 1 0 0 1-.25 1z"/></svg>123 456 7890</li>
      <li><svg viewBox="0 0 24 24"><path d="M6 3h10v5H6zM4 9h16a2 2 0 0 1 2 2v7h-4v3H6v-3H2v-7a2 2 0 0 1 2-2zm4 7v3h8v-3z"/></svg>123 456 7890</li>
      <li><svg viewBox="0 0 24 24"><path d="M2 5h20v14H2zm2 2v.5l8 5 8-5V7zm0 2.8V17h16V9.8l-8 5z"/></svg>Gerald@thequillstoneframeworks.com</li>
    </ul>

    <div class="person">
      <p class="person-name">Gerald Finch</p>
      <p class="person-role">Owner</p>
    </div>

    <address class="address" style="font-style:normal">
      4816 Marlow Ct #306142<br>Houston, TX 77391
    </address>

    <svg class="swoosh" viewBox="0 0 620 120" preserveAspectRatio="none" aria-hidden="true">
      <path d="M0 40 C 180 85, 400 110, 620 116 L620 120 L0 120 Z" fill="var(--rule-grey)"/>
      <path d="M0 58 C 170 98, 380 116, 620 120 L0 120 Z" fill="var(--brand-red)"/>
      <path d="M0 30 C 200 78, 420 104, 620 110" fill="none" stroke="var(--rule-grey)" stroke-width="1.2"/>
    </svg>
  </section>
</main>
</body>
</html>
```